Business Card for Quillmark Ledger - A cannabis publication for executives.

I'd like some business cards for Quillmark Ledger. The logo is done (great job!) and I need a card design I will use with PRINTLY. I made it a short project to allow time for printing before an event. These will be standard sized cards (final artwork size 3.66" x 2.16" at 300dpi) with a final card size of 3.5" x 2.0". (See PRINTLY.com if you need more info.) I might try rounded corners but am not sure yet. I think the design will work okay with rounded.

Quillmark Ledger will be a bi-weekly publication for the cannabis industry. It is targeted to investors and industry executives, not consumers or pot smokers. So our market is more B2B. However I am open to creativity and making the card something people remark on.

My contact for card:

Dana Merrow
Founder/CEO
dana@quillmarkledger.example

2740 Harlow Avenue
Boston MA 02135
(617)555-0194

Target Market(s)

Executives, Industry people and investors in the Cannabis sector.

Contact Information for Business Card

PRINTLY does do double sided and the second side can be the same or different images. Only one side is required but use of the second side would be a bonus.

Font styles to use
Serif
Sans Serif
Decorative

Colors

Designer to choose colors to be used in the design.

Requirements
Must have
• Logo, contact info
Nice to have
• Style and design to make the card stand out in a crowd.

```html
<!DOCTYPE html>
<html lang="en">
<head>
<meta charset="utf-8">
<title>Quillmark Ledger – Business Card</title>
<link rel="stylesheet" href="https://fonts.googleapis.com/css2?family=Source+Sans+3:wght@400;600&display=swap">
<style>
  :root {
    --backdrop: #e2e2e2;
    --card-white: #ffffff;
    --forest: #146636;
    --leaf: #7ac143;
    --lime: #8dc63f;
    --ink: #5a5a5a;
    --ink-soft: #6b6b6b;
  }
  * { margin: 0; padding: 0; box-sizing: border-box; }
  html, body {
    width: 1200px; height: 1200px; overflow: hidden;
    background: var(--backdrop);
    font-family: "Source Sans 3", "Myriad Pro", sans-serif;
  }
  .canvas { position: relative; width: 1200px; height: 1200px; }

  .card {
    position: absolute;
    border-radius: 18px;
    overflow: hidden;
    background: var(--card-white);
  }

  /* Front */
  .card--front { left: 197px; top: 198px; width: 658px; height: 376px; }
  .wordmark {
    position: absolute;
    display: flex; align-items: center; gap: 14px;
    font-weight: 600; white-space: nowrap;
  }
  .wordmark__square { display: block; flex: none; }
  .card--front .wordmark {
    left: 50%; top: 50%; transform: translate(-50%, -50%);
    font-size: 44px; color: var(--forest);
  }
  .card--front .wordmark__square { width: 38px; height: 38px; background: var(--leaf); }

  /* Back */
  .card--back { left: 314px; top: 607px; width: 696px; height: 397px; }
  .brand-panel {
    position: absolute; left: 0; top: 0; width: 381px; height: 100%;
    background: var(--forest);
  }
  .brand-panel__notch {
    position: absolute; left: 381px; top: 80px;
  }
  .card--back .wordmark {
    left: 190px; top: 200px; transform: translate(-50%, -50%);
    font-size: 32px; color: var(--lime); gap: 11px;
  }
  .card--back .wordmark__square { width: 28px; height: 28px; background: var(--lime); }

  .contact { position: absolute; left: 418px; top: 30px; right: 14px; color: var(--ink); }
  .contact__name { font-size: 40px; font-weight: 400; line-height: 1; color: var(--ink); }
  .contact__title { margin-top: 16px; font-size: 16px; color: var(--ink-soft); }
  .contact__list { list-style: none; margin-top: 28px; }
  .contact__item {
    display: flex; align-items: center; gap: 8px;
    font-size: 19px; line-height: 28px; color: var(--ink);
    margin-bottom: 26px; white-space: nowrap;
  }
  .contact__icon { flex: none; width: 34px; height: 28px; }
  .contact__text--email { font-size: 16px; letter-spacing: -0.1px; }
  .contact__item--address { align-items: flex-start; }
  .contact__item--address .contact__text { line-height: 40px; margin-top: -6px; }
</style>
</head>
<body>
<main class="canvas">

  <section class="card card--front" aria-label="Card front">
    <div class="wordmark">
      <span class="wordmark__square"></span>
      <span class="wordmark__name">Quillmark Ledger</span>
    </div>
  </section>

  <section class="card card--back" aria-label="Card back">
    <div class="brand-panel">
      <div class="wordmark">
        <span class="wordmark__square"></span>
        <span class="wordmark__name">Quillmark Ledger</span>
      </div>
    </div>
    <svg class="brand-panel__notch" width="18" height="36" viewBox="0 0 18 36" aria-hidden="true">
      <polygon points="0,0 18,18 0,36" fill="var(--forest)"/>
    </svg>

    <div class="contact">
      <h1 class="contact__name">Dana Merrow</h1>
      <p class="contact__title">Founder/CEO</p>
      <ul class="contact__list">
        <li class="contact__item">
          <svg class="contact__icon" viewBox="0 0 34 28" aria-hidden="true">
            <path d="M7 2c2-1 3 0 4 2l2 4c1 2 0 3-1 4l-1 1c1 3 4 6 7 7l1-1c1-1 2-2 4-1l4 2c2 1 3 2 2 4-2 4-5 5-9 4C12 26 5 19 3 11 2 7 3 4 7 2z" fill="var(--leaf)"/>
          </svg>
          <span class="contact__text">(617)555-0194</span>
        </li>
        <li class="contact__item">
          <svg class="contact__icon" viewBox="0 0 34 28" aria-hidden="true">
            <rect x="1" y="4" width="32" height="21" fill="var(--leaf)"/>
            <polyline points="1,4 17,17 33,4" fill="none" stroke="#fff" stroke-width="2"/>
            <polyline points="1,25 13,14 M21,14 33,25" fill="none" stroke="#fff" stroke-width="2"/>
          </svg>
          <span class="contact__text contact__text--email">dana@quillmarkledger.example</span>
        </li>
        <li class="contact__item contact__item--address">
          <svg class="contact__icon" viewBox="0 0 34 28" aria-hidden="true">
            <polygon points="17,1 33,14 29,14 29,27 21,27 21,18 13,18 13,27 5,27 5,14 1,14" fill="var(--leaf)"/>
          </svg>
          <span class="contact__text">2740 Harlow Avenue<br>Boston MA 02135</span>
        </li>
      </ul>
    </div>
  </section>

</main>
</body>
</html>
```